lighting products eshop web site

We need a brand new ecommerce website (only psd files for the layout) , that will sell professional lighting products in Greek territory.
Please check the sister site www.lampiroxa.gr to get an idea of the products, they will be similar, actually like the products under the menu category "ΕΠΑΓΓΕΛΜΑΤΙΚΑ".
We would like the same philosophy as far as concern the menu structure, namely the menu categories/subcategories shall be actually the products
categories/subcategories, however the menu items shall be presented in a different, more sophisticated way. As far as concern the website layout, we need a minimal, elegant
and contemporary approach that will highlight the products in a perfect manner. We prefer the white color as the main website (background) color and discrete use of brand logo colors.
That is the main idea, awaiting your personal proposal according to the aforementioned requirements
Technically speaking we use bootstrap framework in terms of design meaning 12cols with max width 1170px.
The website will be a joomla - virtuemart website

For images please use some from lampiroxa.gr
For text use any text - just to show me the space.

Industry/Entity Type

It Professional

Number of Pages Required

3 page

Font styles to use
Sans Serif

Colors
00a990
ec1f27

Requirements
Must have
• I need 4 psd pages for the website
• 1. Start page
• 2. Category page
• 3. Product details page
• 4. blog page
Nice to have
• leave designer to choose the best

```html
<!DOCTYPE html>
<html lang="en">
<head>
<meta charset="utf-8">
<title>Lampiroxa – Shopping Cart</title>
<link href="https://fonts.googleapis.com/css2?family=Open+Sans:wght@400;600;700&family=Raleway:wght@300&display=swap" rel="stylesheet">
<style>
:root{
  --red:#ec1f27;--green:#00a990;--orange:#f08a24;
  --dark:#3b3b3b;--btn:#5a5a5a;--text:#555;--muted:#888;
  --line:#e2e2e2;--head-bg:#f4f4f4;--star:#f5b400;--price:#d9222a;
}
*{box-sizing:border-box;margin:0;padding:0}
html,body{width:894px;height:1200px;overflow:hidden}
body{font-family:"Open Sans",sans-serif;color:var(--text);background:#fff;position:relative;font-size:8px}
.abs{position:absolute}
.topbar{left:0;top:0;width:894px;height:22px;background:var(--dark);color:#ccc;font-size:7.5px}
.topbar .tag{position:absolute;left:59px;top:4px;background:var(--orange);color:#fff;padding:2px 6px;border-radius:2px}
.topbar .msg{position:absolute;left:115px;top:6px}
.topbar .menu{position:absolute;right:37px;top:0;display:flex;height:22px}
.topbar .menu span{border-left:1px solid #555;padding:6px 9px}
.header{left:0;top:22px;width:894px;height:98px;background:#f6f6f6;border-bottom:1px solid #ddd}
.hotline{position:absolute;left:59px;top:28px;font-size:7.5px;color:#444;display:flex;align-items:center;gap:5px}
.hotline b{font-weight:700}
.logo{position:absolute;left:0;width:894px;top:20px;text-align:center;font-family:"Raleway",sans-serif;font-weight:300;font-size:24px;letter-spacing:3px;color:var(--red)}
.hbtn{position:absolute;top:22px;width:22px;height:22px;background:var(--red);display:flex;align-items:center;justify-content:center}
.badge{position:absolute;left:829px;top:15px;width:11px;height:11px;border-radius:50%;background:var(--orange);color:#fff;font-size:6px;text-align:center;line-height:11px}
.nav{position:absolute;top:76px;left:0;width:894px;display:flex;justify-content:center;gap:21px;font-weight:700;font-size:7.8px;color:#222}
.new{position:absolute;left:314px;top:62px;background:var(--orange);color:#fff;font-size:5.5px;padding:1px 3px;font-weight:700}
h1{position:absolute;left:59px;top:131px;font-weight:400;font-size:12.5px;color:#444;letter-spacing:.3px}
.cart{left:59px;top:160px;width:776px;height:270px;border:1px solid var(--line)}
.cart table{border-collapse:collapse;width:100%;font-size:7.5px;text-align:center}
.cart th{height:26px;font-weight:400;color:#444;border-right:1px solid var(--line);border-bottom:1px solid var(--line)}
.cart td{height:70px;border-right:1px solid var(--line);border-bottom:1px solid var(--line)}
.cart th:last-child,.cart td:last-child{border-right:0}
.thumb{width:100px;height:56px;margin:auto;border-radius:4px}
.qty{display:inline-block;width:24px;height:23px;border:1px solid #ccc;line-height:21px}
.x{font-weight:700;color:#222;font-size:9px}
.btn{background:var(--btn);color:#fff;font-size:7.5px;padding:5px 9px;display:inline-block;text-transform:uppercase}
.cart .actions{position:absolute;right:7px;bottom:7px;display:flex;gap:3px}
.panel{border:1px solid var(--line);padding:10px}
.panel h3{font-size:8px;font-weight:400;color:#333;margin-bottom:5px}
.panel p,.panel label{font-size:7px;color:#777;display:block}
.field{height:19px;border:1px solid #ddd;margin:4px 0 8px;font-size:7px;color:#666;padding:5px 9px;position:relative}
.field .caret{position:absolute;right:6px;top:4px;font-size:6px}
.rec{left:59px;top:442px;width:246px}
.rec .intro{font-size:7px;color:#666;line-height:1.2;margin-bottom:4px}
.item{display:flex;height:68px;border-bottom:1px solid #ddd;align-items:center;gap:10px}
.item .img{width:60px;height:56px;border-radius:4px}
.item .name{font-size:9px;color:#444;margin:2px 0}
.item .price{color:var(--price);font-weight:600;font-size:10.5px}
.item .old{color:#aaa;font-size:7px;text-decoration:line-through;margin-left:3px}
.stars{color:var(--star);font-size:8px;letter-spacing:-1px}
.stars i{color:#ccc;font-style:normal}
.footer{left:0;top:854px;width:894px;height:314px;background:linear-gradient(180deg,#2c2c2c,#3c3d3a 50%,#262725)}
.fnav{position:absolute;top:20px;left:0;width:894px;display:flex;justify-content:center;gap:26px;color:#fff;font-weight:700;font-size:7.6px}
.frule{position:absolute;left:59px;top:46px;width:776px;height:1px;background:#555}
.flogo{position:absolute;top:70px;width:894px;text-align:center;font-family:"Raleway",sans-serif;font-weight:300;font-size:21px;letter-spacing:3px;color:var(--red)}
.finfo{position:absolute;top:136px;width:894px;text-align:center;color:#bbb;font-size:7.8px;line-height:17px}
.social{position:absolute;top:186px;left:0;width:894px;display:flex;justify-content:center;gap:4px}
.social span{width:26px;height:26px;border:1px solid #fff;border-radius:50%}
.copy{position:absolute;top:264px;width:894px;text-align:center;color:#eee;font-size:7.8px}
.copy em{color:var(--red);font-style:normal}
.cards{position:absolute;top:284px;left:0;width:894px;display:flex;justify-content:center;gap:4px}
.cards span{width:21px;height:13px;background:#bbb;border-radius:2px}
.bottom{left:0;top:1168px;width:894px;height:32px;background:#0d0d0d}
</style>
</head>
<body>

<div class="abs topbar">
  <span class="tag">This Week</span>
  <span class="msg">Aliquam justo mi, lobortis posuere lacus ut, ultricies feugiat nulla</span>
  <div class="menu"><span>👤 My Account ⌄</span><span>Checkout ⌄</span><span>English ⌄</span><span>EUR ⌄</span></div>
</div>

<div class="abs header">
  <div class="hotline">
    <svg width="14" height="10" viewBox="0 0 14 10"><path d="M1 4c0-2 3-3 6-3s6 1 6 3l-2 1-1-2H4L3 5z M3 6h8l1 4H2z" fill="#ec1f27"/></svg>
    <span><b>HOTLINE:</b> (210) 4455 - 1200</span>
  </div>
  <div class="logo">LAMPIROXA</div>
  <div class="hbtn" style="left:783px"><svg width="9" height="9" viewBox="0 0 9 9"><circle cx="3.7" cy="3.7" r="2.7" fill="none" stroke="#fff" stroke-width="1.3"/><path d="M5.7 5.7L8 8" stroke="#fff" stroke-width="1.5"/></svg></div>
  <div class="hbtn" style="left:813px"><svg width="10" height="9" viewBox="0 0 10 9"><path d="M0 1h2l1.5 4.5h5L10 2H3" fill="none" stroke="#fff" stroke-width="1.2"/><circle cx="4" cy="7.7" r="1" fill="#fff"/><circle cx="8" cy="7.7" r="1" fill="#fff"/></svg></div>
  <div class="badge">0</div>
  <span class="new">NEW</span>
  <div class="nav"><span>HANGING</span><span>ROOF</span><span>FLOOR</span><span>WALL</span><span>SPOT</span><span>OUTDOOR</span><span>FANS</span><span>PROFESSIONAL</span><span>COMPANIES</span></div>
</div>

<h1>SHOPPING CART</h1>

<div class="abs cart">
  <table>
    <tr><th style="width:153px"></th><th style="width:207px">Product Name</th><th style="width:63px"></th><th style="width:112px">Unit Price</th><th style="width:83px">Qty</th><th style="width:111px">Subtotal</th><th></th></tr>
    <tr><td><div class="thumb" role="img" aria-label="Dark bowl pendant lamp" style="background:radial-gradient(ellipse at 50% 55%,#5a3a36,#c9a89c 60%,#fff 75%)"></div></td><td>Molaz tren open zase</td><td>Edit</td><td>$120.00</td><td><span class="qty">1</span></td><td>$120.00</td><td class="x">×</td></tr>
    <tr><td><div class="thumb" role="img" aria-label="Crystal bar chandelier" style="background:linear-gradient(180deg,#fff,#cfd7dc 40%,#9aa7b0 80%,#fff)"></div></td><td>Ires mite rima</td><td>Edit</td><td>$168.00</td><td><span class="qty">1</span></td><td>$168.00</td><td class="x">×</td></tr>
    <tr><td><div class="thumb" role="img" aria-label="Candle style chandelier" style="background:radial-gradient(ellipse,#e8dcc0,#f6f1e4 55%,#fff 75%)"></div></td><td>Cori miren masem</td><td>Edit</td><td>$5,568.00</td><td><span class="qty">1</span></td><td>$5,568.00</td><td class="x">×</td></tr>
  </table>
  <div class="actions"><span class="btn">Continue Shopping</span><span class="btn">Update Shopping Cart</span><span class="btn">Clear Shopping Cart</span></div>
</div>

<div class="abs rec">
  <p class="intro">Based on your selection, you may be interested in the following items:</p>
  <div class="item"><div class="img" role="img" aria-label="Black cone pendant lamp" style="background:radial-gradient(ellipse at 50% 70%,#333,#fff 60%)"></div><div><div class="stars">★★★★<i>★</i></div><div class="name">Rika mire pisan</div><div class="price">$753.00</div></div></div>
  <div class="item"><div class="img" role="img" aria-label="Bowl pendant lamp" style="background:radial-gradient(ellipse,#5a3a36,#c9a89c 55%,#fff 72%)"></div><div><div style="font-size:6.5px;color:#999">Write Your Review</div><div class="name">Xemi irem masen</div><div class="price">$520.00</div></div></div>
  <div class="item"><div class="img" role="img" aria-label="Candle chandelier" style="background:radial-gradient(ellipse,#e8dcc0,#fff 70%)"></div><div><div class="stars">★★★★<i>★</i></div><div class="name">Kesa mirem pikam</div><div class="price">$500.00<span class="old">$550.00</span></div></div></div>
  <div class="item" style="border:0"><div class="img" role="img" aria-label="Crystal chandelier" style="background:linear-gradient(180deg,#fff,#bcc6cd 50%,#fff)"></div><div><div class="stars">★★★<i>★★</i></div><div class="name">Pisan maze ikan</div><div class="price">$130.00<span class="old">$155.00</span></div></div></div>
</div>

<div class="abs panel" style="left:325px;top:442px;width:245px;height:104px">
  <h3>DISCOUNT CODES</h3>
  <p>Enter your coupon code if you have one.</p>
  <div class="field"></div>
  <div style="text-align:right;margin-top:12px"><span class="btn">Apply Coupon</span></div>
</div>

<div class="abs panel" style="left:325px;top:560px;width:245px;height:278px">
  <h3>ESTIMATE SHIPPING AND TAX</h3>
  <p>Enter your destination to get a shipping estimate.</p>
  <label>Country<span style="color:var(--red)">*</span></label>
  <div class="field">United States<span class="caret">▼</span></div>
  <label>State/Province</label>
  <div class="field">Please select region, state or province<span class="caret">▼</span></div>
  <label>City</label><div class="field"></div>
  <label>Zip/Postal Code</label><div class="field"></div>
  <div style="border-top:1px solid #eee;text-align:right;padding-top:6px"><span class="btn">Get A Quote</span></div>
  <p style="margin-top:6px">Free Shipping</p>
  <p>◯ &nbsp;Free $0.00</p>
  <div style="border-top:1px solid #eee;text-align:right;padding-top:7px;margin-top:5px"><span class="btn">Update Total</span></div>
</div>

<div class="abs panel" style="left:590px;top:442px;width:245px;height:80px;font-size:7.5px">
  <div style="display:flex;justify-content:space-between;color:#666"><span>Subtotal</span><span>$5,856.00</span></div>
  <div style="display:flex;justify-content:space-between;color:#333;font-weight:600;margin-top:8px"><span>Grand Total</span><span>$5,856.00</span></div>
  <div style="text-align:right;margin-top:6px"><span class="btn">Proceed To Checkout</span></div>
</div>

<div class="abs footer" role="img" aria-label="Aerial view of the company warehouse at dusk">
  <div class="fnav"><span>COMPANY</span><span>SHOP</span><span>COOPERATING COMPANIES</span><span>DATA PROTECTION</span><span>TERMS OF USE</span><span>PAYMENT METHOD</span><span>SHIPPING METHOD</span><span>RETURN POLICY</span><span>CONTACT US</span></div>
  <div class="frule"></div>
  <div class="flogo">LAMPIROXA</div>
  <div style="position:absolute;top:100px;width:894px;text-align:center;color:#999;font-size:8px;letter-spacing:3px">• • •</div>
  <div class="finfo">27, Ermou Street, Athens, Greece / Telephone: (210) 4455 - 1201<br>E-mail: support@lampiroxa.gr</div>
  <div class="social"><span aria-label="Social link 1"></span><span aria-label="Social link 2"></span><span aria-label="Social link 3"></span><span aria-label="Social link 4"></span><span aria-label="Social link 5"></span></div>
  <div class="copy">© 2016 Lampiroxa Store. All Rights Reserved. Designed by <em>Brightline Studio</em></div>
  <div class="cards" aria-label="Accepted payment methods"><span></span><span></span><span></span><span></span><span></span><span></span></div>
</div>
<div class="abs bottom"></div>

</body>
</html>
```